Website Page Re-Design

I have 2 pages that need to be re-designed on my site. This is the site so you can take a look and get a feel for the layout etc, www.vortaplay.com
I have included screen shots of the individual pages I want redone as well as some examples from other sites for ideas.

Homepage Story, would like the redo sunday file, to be made stunning, only the content, picture and share buttons need be altered the, would like and emphasis on intergrating the share buttons, the story page starts here http://www.vortaplay.com/league/ball-hockey/mens/news-division/ so what is beingcreated is when the read more is clicked

Free Agent Forms:
Needs to be re-worked so that there isn't so much white space on the page.

Industry/Entity Type

News

Requirements
Must have
• share buttons to slick very well intergrated
Nice to have
• Share buttons to be top notch

```html
<!DOCTYPE html>
<html lang="en">
<head>
<meta charset="utf-8">
<title>Vortaplay Sports – Home</title>
<link rel="stylesheet" href="https://fonts.googleapis.com/css2?family=Questrial&display=swap">
<style>
:root{
  --green-dark:#3f6f0a;
  --green:#4f7f12;
  --green-light:#5e9418;
  --yellow:#e7c92a;
  --yellow-dark:#c9a915;
  --yellow-light:#f4df55;
  --nav-active:#f2e15a;
  --text:#333333;
  --muted:#8a8a8a;
  --btn:#3b6a0d;
  --btn-text:#f3e36a;
  --white:#ffffff;
}
*{margin:0;padding:0;box-sizing:border-box}
html,body{width:1000px;height:1200px;overflow:hidden;background:var(--white)}
body{position:relative;font-family:"Questrial",sans-serif;color:var(--text)}

.site-header{position:absolute;left:0;top:0;width:1000px;height:88px;
  background:linear-gradient(#5a8c17,var(--green-dark));}
.brand{position:absolute;left:117px;top:24px;display:flex;align-items:center;gap:8px;
  color:#eef3c0;font-size:34px;letter-spacing:.5px}
.brand-dot{width:12px;height:12px;background:var(--yellow);border-radius:50%}
.top-nav{position:absolute;right:117px;top:27px;font-size:11.5px;color:var(--white);display:flex;gap:11px}
.top-nav a{color:var(--white);text-decoration:none}
.top-nav a.active{color:var(--nav-active)}
.top-nav .sep{opacity:.9}

.main-nav{position:absolute;left:313px;top:71px;width:569px;height:36px;
  background:linear-gradient(var(--yellow-light),var(--yellow) 55%,var(--yellow-dark));
  border:1px solid #a98f10;border-radius:3px;display:flex;z-index:2}
.main-nav a{flex:auto;display:flex;align-items:center;justify-content:center;
  font-size:12.5px;font-weight:bold;color:#2d3a05;text-decoration:none;border-right:1px solid #c2a61a;letter-spacing:.2px}
.main-nav a:last-child{border-right:0}

.hero{position:absolute;left:0;top:88px;width:1000px;height:420px;border-top:3px solid var(--yellow);display:flex}
.hero-panel{width:250px;height:100%}
.hero-panel.football{background:linear-gradient(160deg,#3a4452,#1f2630 60%,#4c5a2c)}
.hero-panel.soccer{background:linear-gradient(170deg,#4a5260,#2a2f38 55%,#5a6a48)}
.hero-panel.fieldhockey{background:linear-gradient(180deg,#2c3138,#3c4a3a 55%,#5a8a3a)}
.hero-panel.highjump{background:linear-gradient(180deg,#7fb3dc,#9cc6e6 60%,#c9a278)}
.hero-arrows{position:absolute;right:162px;bottom:8px;display:flex;gap:3px}
.hero-arrows span{width:24px;height:24px;background:#1f1f1f;display:flex;align-items:center;justify-content:center}

.section-title{position:absolute;font-size:23px;color:#333}
.story-photo{position:absolute}
.story-head{position:absolute;font-size:14.5px;color:#222;letter-spacing:.3px}
.share{position:absolute;display:flex;gap:2px}
.share i{display:block;width:11px;height:11px;border-radius:2px}
.share .s1{background:#3b5b98}.share .s2{background:#44a7dc}.share .s3{background:#5b9d3b}.share .s4{background:#e9573f}
.copy{position:absolute;font-size:11.6px;line-height:15.6px;color:var(--muted)}
.read-more{position:absolute;width:78px;height:21px;background:var(--btn);color:var(--btn-text);
  font-size:11.5px;display:flex;align-items:center;justify-content:center;border-radius:2px;text-decoration:none}

.site-footer{position:absolute;left:0;top:1122px;width:1000px;height:78px;background:var(--green);color:var(--white);font-size:11px}
.footer-nav{position:absolute;left:117px;top:14px;display:flex;gap:10px}
.footer-nav a{color:var(--white);text-decoration:none}
.footer-contact{position:absolute;left:117px;top:35px;line-height:18px}
.footer-find{position:absolute;left:536px;top:14px}
.social{position:absolute;left:536px;top:40px;display:flex;gap:7px}
.social span{width:22px;height:22px;border-radius:50%;background:#111}
.newsletter-title{position:absolute;left:708px;top:14px}
.newsletter{position:absolute;left:708px;top:40px;display:flex;gap:5px}
.newsletter input{width:136px;height:21px;background:#3c6410;border:1px solid #32550c;color:#9fb25a;font-family:inherit;font-size:9px;padding:0 6px}
.newsletter button{width:34px;height:21px;background:#3c6410;border:1px solid #32550c;color:var(--white);font-family:inherit;font-size:11px}
</style>
</head>
<body>

<header class="site-header">
  <div class="brand"><span>Vortaplay</span><span class="brand-dot"></span></div>
  <nav class="top-nav">
    <a class="active" href="#">HOME</a><span class="sep">/</span>
    <a href="#">ABOUT US</a><span class="sep">/</span>
    <a href="#">FAQS</a><span class="sep">/</span>
    <a href="#">CONTACT US</a><span class="sep">/</span>
    <a href="#">JOBS</a><span class="sep">/</span>
    <a href="#">SPONSORS</a>
  </nav>
</header>

<nav class="main-nav">
  <a href="#">LEAGUES</a><a href="#">SCHEDULES &amp; MOR</a><a href="#">REGISTER</a><a href="#">PAY</a><a href="#">FORUM</a><a href="#">TOURNAMENTS</a>
</nav>

<section class="hero">
  <div class="hero-panel football" role="img" aria-label="Football players in uniform on a stadium field"></div>
  <div class="hero-panel soccer" role="img" aria-label="Soccer players competing for the ball"></div>
  <div class="hero-panel fieldhockey" role="img" aria-label="Field hockey player with stick and ball on grass"></div>
  <div class="hero-panel highjump" role="img" aria-label="Athlete clearing a high jump bar"></div>
  <div class="hero-arrows">
    <span><svg width="8" height="12" viewBox="0 0 8 12"><path d="M6 1L1.5 6 6 11" stroke="#fff" stroke-width="2" fill="none"/></svg></span>
    <span><svg width="8" height="12" viewBox="0 0 8 12"><path d="M2 1l4.5 5L2 11" stroke="#fff" stroke-width="2" fill="none"/></svg></span>
  </div>
</section>

<h2 class="section-title" style="left:117px;top:533px">Story</h2>

<div class="story-photo" style="left:119px;top:579px;width:355px;height:183px;background:linear-gradient(90deg,#e8e8e8,#d9dde6 55%,#2f4fa6)" role="img" aria-label="Ball hockey team posing together with a large cheque"></div>
<h3 class="story-head" style="left:117px;top:782px">Ball Hockey</h3>
<div class="share" style="left:415px;top:783px"><i class="s1"></i><i class="s2"></i><i class="s3"></i><i class="s4"></i></div>
<p class="copy" style="left:117px;top:808px;width:360px">At Vortaplay Sports, you can find a ball hockey league that fits into your schedule. We offer men’s competitive, co-ed, and pick-up games for men and women. Ball hockey leagues are available on multiple nights at various gyms inside our facility, with each game an hour in length.</p>
<a class="read-more" style="left:398px;top:880px" href="#">Read More</a>

<div class="story-photo" style="left:524px;top:579px;width:359px;height:186px;background:linear-gradient(180deg,#4d7d3a,#6f9a4e 45%,#c9a982 60%,#6c9a44)" role="img" aria-label="Slo-pitch pitcher winding up on a ball diamond"></div>
<h3 class="story-head" style="left:524px;top:782px">Co-ed Slo-Pitch</h3>
<div class="share" style="left:822px;top:783px"><i class="s1"></i><i class="s2"></i><i class="s3"></i><i class="s4"></i></div>
<p class="copy" style="left:524px;top:808px;width:362px">Vortaplay Sports is proud to offer Co-Ed Slo-Pitch to the community of Calgary. Since 2011, Slo-Pitch has been a great opportunity for men and women in the Calgary area to enjoy the game they love. Vortaplay Sports offers co-ed Slo-Pitch leagues from early May to September, and games..</p>
<a class="read-more" style="left:805px;top:880px" href="#">Read More</a>

<h2 class="section-title" style="left:117px;top:928px;font-size:19px">What Is Vortaplay Sports All About?</h2>
<p class="copy" style="left:117px;top:958px;width:362px">Since 2007, Vortaplay Sports has been providing sports activities such as slo-pitch/softball and ball hockey to the Calgary area. Many of our leagues are co-ed, however, we do provide competitive ball hockey as well. The goal of Vortaplay Sports is to promote an interactive and social atmosphere to all of our members as part of a sports club. The entire experience is about having fun!</p>
<a class="read-more" style="left:397px;top:1047px" href="#">Read More</a>

<h2 class="section-title" style="left:524px;top:928px;font-size:19px">Vortaplay News</h2>
<div class="story-photo" style="left:524px;top:961px;width:196px;height:129px;background:linear-gradient(90deg,#6aa83a,#5b9632 55%,#8a6a52)" role="img" aria-label="Ball hockey fall registration promotional banner"></div>
<h3 class="story-head" style="left:735px;top:958px;font-size:13.5px">Co-ed Slo-Pitch</h3>
<p class="copy" style="left:735px;top:984px;width:150px">Fall 2013 Ball Hockey! Don't know what to do with yourself now that Calgary's Slo-Pitch season is coming to an end? How about reg­istering for one of our floor hockey leagues?.</p>

<footer class="site-footer">
  <nav class="footer-nav">
    <a href="#">ABOUT US</a><span>/</span><a href="#">FAQS</a><span>/</span><a href="#">CONTACT US</a><span>/</span><a href="#">JOBS</a><span>/</span><a href="#">SPONSORS</a>
  </nav>
  <div class="footer-contact">E mail : info@vortaplay.com<br>© 2011-2012, Sports. All Rights Reserved</div>
  <div class="footer-find">FIND US ON SIDE</div>
  <div class="social"><span></span><span></span><span></span></div>
  <div class="newsletter-title">SIGN UP TO OUR NEWSLETTER!</div>
  <form class="newsletter"><input type="text" placeholder="email address"><button type="button">GO</button></form>
</footer>

</body>
</html>
```